Etiketten für Honiggläser gesucht
sehr kreativer Entwurf, in dem alle umfangreichen Vorgaben berücksichtigt wurden. q4472 ist sehr service- und lösungsorientiert. Arbeitet sehr schnell und exzellent.
Zielgruppe
Wir sind eine junge Hobbyimkerei und produzieren unsere eigenen Honigsorten. Zielgruppe ist jeder, der Honig mag.
Aufgabenstellung
Das zu entwerfende Etiketten_Design soll grundsätzlich ein „absoluter Hingucker“ werden, einen hohen Wiedererkennungswert besitzen, edel erscheinen und die Hochwertigkeit des Produktes zum Ausdruck bringen.
Im engeren Sinn sollen zwei voneinander unabhängige Etikettenteile entworfen werden, die aber im Design eine Einheit bilden sollen:
Beim ersten Teil handelt es sich um den sogenannten Gewährverschluss; er verbindet den Deckel mit dem Glas und zerreißt beim ersten Öffnen des Deckels. Der Gewährverschluss soll etwa 2 cm breit und 8 cm lang sein, und unter anderem von unserem Firmenlogo (siehe Datei) geziert werden. Bei dem Logo darf die Grafik und der Hintergrund in der Farbe variieren, und der Schriftzug kann entfallen, andere Änderungen dürfen jedoch nicht vorgenommen werden. Das Logo kann bei Bedarf gerne in anderen Dateiformaten zur Verfügung gestellt werden.
Den zweiten Teil stellt das eigentliche Produktetikett dar. Für dieses gibt es keine Größen- und Formvorgaben, allerdings müssen folgende Inhalte Berücksichtigung finden: Die Daten des Imkers (bitte folgende Platzhalter verwenden „Firmenname“, „Vorname1 & Vorname2 Nachname“, „Straße + Hausnummer“, „PLZ + Ortsname“, „Internetseite“ und „Emailadresse“) sowie den Angaben „500g“, „Mindestens haltbar bis:“ (dahinter oder darunter bitte weißen Freiraum für den Stempelaufdruck des Datums lassen), „Trocken, dunkel und vor Wärme geschützt lagern!“, und – ganz wichtig – die „Honigsorte“ mit den vorangestellten Worten „feinster deutscher“ (, z.B. „feinster deutscher Rapshonig“).
Jede Honigsorte soll mit einer Farbe verknüpft werden, sodass der Kunde schnell erkennen kann um welche Honigsorte es sich im Glas handelt (beispielsweise gelb für Rapshonig, grün für Waldhonig, usw.). Dafür soll die jeweilige Honigsortenfarbe, in welcher Form auch immer, das Etikett oder einen bestimmten Bereich davon domini..

```html
<!DOCTYPE html>
<html lang="de">
<head>
<meta charset="utf-8">
<title>Imkerei Lindholm – Honigetiketten</title>
<link rel="stylesheet" href="https://fonts.googleapis.com/css2?family=Dancing+Script:wght@500&family=Itim&family=Source+Sans+3:wght@400&family=Cormorant+SC:wght@600&display=swap">
<style>
  :root {
    --bg: #ffffff;
    --ink: #2a2a2a;
    --raspberry: #c0144a;
    --forest-ring: #3f8f58;
    --forest-text: #0c6a35;
    --seal: #1c1c1c;
  }
  html, body {
    margin: 0;
    padding: 0;
    width: 1200px;
    height: 848px;
    overflow: hidden;
    background: var(--bg);
  }
  .canvas { display: block; width: 1200px; height: 848px; }
  .label-fill { fill: #ffffff; }
  .inner-rule { fill: none; stroke: var(--ink); stroke-width: 1; }
  .tagline { font-family: "Dancing Script", cursive; font-size: 31px; fill: var(--ink); }
  .note { font-family: "Source Sans 3", sans-serif; font-size: 9px; fill: var(--ink); }
  .contact { font-family: "Source Sans 3", sans-serif; font-size: 10.5px; fill: var(--ink); letter-spacing: 0.4px; text-anchor: end; }
  .date-box { fill: #ffffff; stroke: var(--ink); stroke-width: 0.8; }
  .weight { font-family: "Source Sans 3", sans-serif; font-size: 20px; fill: var(--ink); }
  .brand { font-family: "Cormorant SC", serif; font-weight: 600; font-size: 25px; fill: var(--ink); letter-spacing: 4px; text-anchor: middle; }
  .brand-dot { fill: none; stroke: var(--ink); stroke-width: 3; }
  .variety { font-family: "Itim", sans-serif; font-size: 42px; letter-spacing: 2px; }
  .raspberry .ring { fill: none; stroke: var(--raspberry); stroke-width: 6; }
  .raspberry .variety { fill: var(--raspberry); }
  .forest .ring { fill: none; stroke: var(--forest-ring); stroke-width: 6; }
  .forest .variety { fill: var(--forest-text); }
  .seal-strip { fill: var(--seal); }
</style>
</head>
<body>
<svg class="canvas" viewBox="0 0 1200 848" xmlns="http://www.w3.org/2000/svg">
  <defs>
    <path id="tagline-arc" d="M -188,-38 A 192,112 0 0 1 188,-38"/>
    <path id="variety-arc" d="M -140,100 Q 0,150 150,78"/>
  </defs>

  <!-- tamper seal -->
  <path class="seal-strip" d="M 196 210 H 244 V 420 L 220 396 L 196 420 Z"/>

  <!-- raspberry label -->
  <g class="label raspberry" transform="translate(798 235)">
    <ellipse class="label-fill ring" rx="247" ry="161"/>
    <ellipse class="inner-rule" rx="233" ry="150"/>
    <text class="tagline"><textPath href="#tagline-arc" startOffset="50%" text-anchor="middle">feinster deutscher Himbeerhonig</textPath></text>
    <text class="note" x="-217" y="-15">Trocken, dunkel und vor</text>
    <text class="note" x="-217" y="-3">Wärme geschützt lagern</text>
    <text class="note" x="-217" y="12">Mindestens haltbar bis:</text>
    <rect class="date-box" x="-217" y="20" width="95" height="22" rx="2"/>
    <text class="weight" x="-198" y="66">500G.</text>
    <text class="contact" x="216" y="-24">Ahornweg 14</text>
    <text class="contact" x="216" y="-9">3012 Talberg</text>
    <text class="contact" x="216" y="6">www.imkereilindholm.de</text>
    <text class="contact" x="216" y="22">@imkereilindholm.de</text>
    <circle class="brand-dot" cx="0" cy="-36" r="36"/>
    <text class="brand" x="0" y="48">IMKEREI</text>
    <text class="brand" x="0" y="78">LINDHOLM</text>
    <text class="variety"><textPath href="#variety-arc" startOffset="50%" text-anchor="middle">Himbeerhonig</textPath></text>
  </g>

  <!-- forest honey label -->
  <g class="label forest" transform="translate(794 637)">
    <ellipse class="label-fill ring" rx="250" ry="161"/>
    <ellipse class="inner-rule" rx="236" ry="150"/>
    <text class="tagline"><textPath href="#tagline-arc" startOffset="50%" text-anchor="middle">feinster deutscher Waldhonig</textPath></text>
    <text class="note" x="-220" y="-15">Trocken, dunkel und vor</text>
    <text class="note" x="-220" y="-3">Wärme geschützt lagern</text>
    <text class="note" x="-220" y="12">Mindestens haltbar bis:</text>
    <rect class="date-box" x="-220" y="20" width="95" height="22" rx="2"/>
    <text class="weight" x="-201" y="66">500G.</text>
    <text class="contact" x="218" y="-24">Ahornweg 14</text>
    <text class="contact" x="218" y="-9">3012 Talberg</text>
    <text class="contact" x="218" y="6">www.imkereilindholm.de</text>
    <text class="contact" x="218" y="22">@imkereilindholm.de</text>
    <circle class="brand-dot" cx="0" cy="-36" r="36"/>
    <text class="brand" x="0" y="48">IMKEREI</text>
    <text class="brand" x="0" y="78">LINDHOLM</text>
    <text class="variety"><textPath href="#variety-arc" startOffset="50%" text-anchor="middle">Waldhonig</textPath></text>
  </g>
</svg>
</body>
</html>
```